Business card

Hi Marta,
can you please design business cards for me?
Based on your Brimvale design please go crazy (still retain a professional business-solid profile). I would like to use really stylish paper (or different paper types and special prints like partly embossed or partly glossy and contrast the glossiness with matt for instance).
Please keep in mind that I might come back to you in several months if the business requires other print material like stationary, folders, envelopes etc. It all needs to be in line and make a huge impression without going over board and still remain very solid and serious.
I know that's a lot to ask and I apologise but I am really impressed with your work so far and have no doubt that you can spin the wheels again in a great way.
Thanks bunches, Lukas
In order to punch in the right text from the outset, here is some key data:
Brimvale
Your next level
Lukas Brander
Chief Executive Level Lifter
+41 79 583 1067
lukas.brander@brimvale.com
brimvale.com
Business
Brimvale
Your next level
Lukas Brander
+41 79 583 1067
brimvale.com

```html
<!DOCTYPE html>
<html lang="en">
<head>
<meta charset="utf-8">
<title>Brimvale – Business Card</title>
<link rel="stylesheet" href="https://fonts.googleapis.com/css2?family=Cabin:wght@400;500;600&display=swap">
<style>
  :root {
    --backdrop: #e4e6e8;
    --card-black: #0c0f14;
    --edge-cyan: #5fc6d9;
    --accent-blue: #2f9fd3;
    --ink-white: #f2f4f6;
    --ink-soft: #c9ced4;
  }
  html, body {
    margin: 0;
    width: 1200px;
    height: 800px;
    overflow: hidden;
    background: var(--backdrop);
  }
  .canvas {
    width: 1200px;
    height: 800px;
    display: flex;
    align-items: center;
    justify-content: center;
    gap: 70px;
    font-family: "Cabin", "Gill Sans", sans-serif;
  }
  .card {
    position: relative;
    width: 490px;
    height: 280px;
    background: var(--card-black);
    box-sizing: border-box;
    border: 4px solid var(--edge-cyan);
    box-shadow: 0 14px 30px rgba(0, 0, 0, 0.18);
  }

  /* Front */
  .card-front {
    display: flex;
    flex-direction: column;
    align-items: center;
    justify-content: center;
    gap: 14px;
  }
  .brand-disc {
    width: 66px;
    height: 66px;
    border-radius: 50%;
    background: var(--ink-white);
  }
  .brand-name {
    color: var(--ink-white);
    font-size: 15px;
    font-weight: 500;
    letter-spacing: 0.22em;
    text-transform: uppercase;
  }

  /* Back */
  .card-back {
    padding: 36px 34px 0 34px;
    color: var(--ink-white);
    white-space: nowrap;
  }
  .holder-name {
    margin: 0;
    font-size: 20px;
    font-weight: 600;
    letter-spacing: 0.12em;
    line-height: 1.1;
    text-transform: uppercase;
  }
  .contact-links {
    margin-top: 10px;
    color: var(--ink-soft);
    font-size: 11px;
    letter-spacing: 0.08em;
    text-transform: uppercase;
  }
  .contact-links .divider {
    margin: 0 8px;
  }
  .holder-title {
    margin-top: 10px;
    text-align: right;
    color: var(--ink-white);
    font-size: 11px;
    letter-spacing: 0.1em;
    text-transform: uppercase;
  }
  .accent-rule {
    height: 1px;
    background: var(--accent-blue);
    margin-top: 7px;
  }
  .phone {
    margin-top: 8px;
    text-align: right;
    color: var(--accent-blue);
    font-size: 11px;
    letter-spacing: 0.12em;
  }
</style>
</head>
<body>
  <main class="canvas">
    <section class="card card-front" aria-label="Business card front">
      <div class="brand-disc"></div>
      <span class="brand-name">Brimvale</span>
    </section>

    <section class="card card-back" aria-label="Business card back">
      <h1 class="holder-name">Lukas Brander</h1>
      <div class="contact-links">lukas.brander@brimvale.com<span class="divider">|</span>brimvale.com</div>
      <div class="holder-title">Chief Executive Level Lifter</div>
      <div class="accent-rule"></div>
      <div class="phone">+41 79 583 1067</div>
    </section>
  </main>
</body>
</html>
```